Geschäftspapiere für Lasergravuren
Zielgruppe
Lasergravuren z.B. auf Glas, Holz, Filz, Papier, Acryl, eloxierten Aluminium zu Dekorationszwecken,
Ausschneiden von Elementen z.B. aus Holz, Filz, Papier, Acryl usw. zu Dekorationszwecken mit dem Lasergravierer.
Anfertigung verschiedener Dekorationsartikel,
Zielgruppe: Frauen (mit Familien) aller Altersgruppen, die Freude am Dekorieren und Verschenken haben
Aufgabenstellung
Das vorhandene Logo soll mit eingebunden werden

```html
<!DOCTYPE html>
<html lang="de">
<head>
<meta charset="utf-8">
<title>Lumora Laser Deko – Briefbogen</title>
<link href="https://fonts.googleapis.com/css2?family=Open+Sans:wght@300;400;600&display=swap" rel="stylesheet">
<style>
  :root {
    --backdrop: #e9e9ea;
    --paper: #ffffff;
    --ink: #3a3a3a;
    --grey: #707070;
    --gold: #b58946;
    --rule: #555555;
  }
  * { box-sizing: border-box; margin: 0; padding: 0; }
  html, body {
    width: 1200px; height: 1010px; overflow: hidden;
    background: var(--backdrop);
    font-family: "Open Sans", sans-serif;
    color: var(--ink);
  }
  .letterhead {
    position: absolute; left: 260px; top: 25px;
    width: 679px; height: 960px;
    background: var(--paper);
    box-shadow: 0 6px 22px rgba(0,0,0,.12);
    overflow: hidden;
  }
  .brand {
    position: absolute; left: 400px; top: 38px;
    display: flex; align-items: center; gap: 10px;
  }
  .brand-mark {
    width: 40px; height: 40px; border-radius: 50%;
    border: 2px solid var(--gold);
  }
  .brand-name {
    font-weight: 300; font-size: 44px; letter-spacing: 1px;
    color: var(--grey); line-height: 1;
  }
  .sender {
    position: absolute; left: 452px; top: 118px;
    padding-left: 12px; border-left: 1px solid var(--rule);
    font-size: 8.6px; line-height: 12px;
  }
  .sender .gap { height: 7px; }
  .sender .icon-line { display: flex; align-items: center; gap: 5px; }
  .sender svg { width: 8px; height: 8px; flex: none; }
  .return-line {
    position: absolute; left: 70px; top: 238px;
    font-size: 7px; border-bottom: 1px solid var(--ink);
    padding-bottom: 1px;
  }
  .return-line .sep { color: var(--gold); padding: 0 2px; }
  .fold-mark {
    position: absolute; left: 0; width: 14px; height: 1px;
    background: #9a9a9a;
  }
  .footer-bands { position: absolute; left: 0; top: 0; width: 679px; height: 960px; }
  .footer-seal {
    position: absolute; left: 118px; top: 872px;
    width: 62px; height: 62px; border-radius: 50%;
    background: var(--paper); border: 3px solid var(--grey);
  }
  .web {
    position: absolute; left: 652px; top: 760px;
    transform: rotate(-90deg); transform-origin: left top;
    color: var(--paper); font-size: 12px; letter-spacing: .5px;
    white-space: nowrap;
  }
</style>
</head>
<body>
<main class="letterhead">
  <div class="brand">
    <span class="brand-mark"></span>
    <span class="brand-name">Lumora</span>
  </div>

  <address class="sender" style="font-style:normal">
    <div>Lumora Laser Deko</div>
    <div>Muster Weg 32</div>
    <div>10400 Muster Stadt</div>
    <div class="gap"></div>
    <div class="icon-line">
      <svg viewBox="0 0 10 10"><path d="M2 1 L4 1 L5 3.5 L3.8 4.5 Q4.8 6.2 5.5 6.2 L6.5 5 L9 6 L9 8 Q5 9.5 1.5 4.5 Z" fill="#b58946"/></svg>
      <span>+49 (0) 4100 7070 - 210</span>
    </div>
    <div class="icon-line">
      <svg viewBox="0 0 10 10"><rect x="1" y="3" width="8" height="5" fill="#b58946"/><rect x="3" y="1" width="4" height="2" fill="#b58946"/></svg>
      <span>+49 (0) 4100 7070 - 213</span>
    </div>
    <div class="icon-line">
      <svg viewBox="0 0 10 10"><rect x="0.5" y="2" width="9" height="6" fill="#b58946"/><path d="M0.5 2 L5 5.5 L9.5 2" stroke="#fff" stroke-width="0.8" fill="none"/></svg>
      <span>info@lumora-beispiel.de</span>
    </div>
    <div class="gap"></div>
    <div>Bankverbindung:</div>
    <div>Bank: Beispielbank Nord eG</div>
    <div>BIC: BEISDEXX000</div>
    <div>IBAN: DE00 1234 5678 9012 3456 78</div>
    <div class="gap"></div>
    <div>SteuerID: DE000111222</div>
    <div>Umsatzsteuer ID: 00 000 111 222</div>
  </address>

  <div class="return-line">Lumora Laser Deko<span class="sep">|</span>Muster Weg 32<span class="sep">|</span>10400 Muster Stadt</div>

  <span class="fold-mark" style="top:340px"></span>
  <span class="fold-mark" style="top:480px"></span>
  <span class="fold-mark" style="top:660px"></span>

  <svg class="footer-bands" viewBox="0 0 679 960" aria-hidden="true">
    <path d="M0 930 C 300 915, 585 820, 620 560 L 642 552 C 612 830, 330 945, 0 960 Z" fill="var(--grey)"/>
    <path d="M150 960 C 420 930, 640 800, 648 548 L 679 538 L 679 960 Z" fill="var(--gold)"/>
  </svg>
  <div class="footer-seal"></div>
  <div class="web">www.lumora-beispiel.de</div>
</main>
</body>
</html>
```